A start up Private Wine Label for export to Asia.

We are looking for the best graphic design for our very first wine label Corvessa Cellars and would like the following requirements:

1. Black background - explore and play around the shade of black
2. Gold Shimmery Colour Font
3. Font should be a cursive classic posh that says Corvessa Cellars
4. We would like the front graphic design to be simple and elegant and has a traditional classic feel to it.

Target Market(s)

Small scale to test the upper class market for export to Asia

Font styles to use
Script

Colors

Designer to choose colors to be used in the design.

Requirements
Must have
• Gold font for the label Corvessa Cellars with shimmery touch to it.
• Elegant black background.
• Simple but elegant design.
• Attractive to the upper class market in Asia.
Nice to have
• Explore and play around with your imagination.

```html
<!DOCTYPE html>
<html lang="en">
<head>
<meta charset="utf-8">
<title>Corvessa Cellars – Front Label</title>
<link rel="stylesheet" href="https://fonts.googleapis.com/css2?family=Great+Vibes&family=Playfair+Display:ital,wght@1,400&display=swap">
<style>
  :root {
    --page: #ffffff;
    --gold-deep: #b07f2e;
    --gold-mid: #d6ab5c;
    --gold-light: #f3de8a;
    --frame-grey: #39393c;
    --panel-black: #1f1f21;
    --panel-glow: #323236;
    --ornament: #2c2c2f;
  }
  html, body {
    margin: 0;
    width: 1200px;
    height: 1200px;
    overflow: hidden;
    background: var(--page);
  }
  .canvas {
    width: 1200px;
    height: 1200px;
    display: flex;
    align-items: center;
    justify-content: center;
  }
  .label {
    width: 784px;
    height: 1120px;
    display: block;
  }
  .brand-name {
    font-family: "Great Vibes", cursive;
    font-size: 150px;
  }
  .volume-line {
    font-family: "Playfair Display", serif;
    font-style: italic;
    font-size: 40px;
    letter-spacing: 1px;
  }
</style>
</head>
<body>
<main class="canvas">
  <svg class="label" viewBox="0 0 944 1348" xmlns="http://www.w3.org/2000/svg" aria-label="Corvessa Cellars wine label">
    <defs>
      <linearGradient id="gold-band" x1="0" y1="0" x2="1" y2="0">
        <stop offset="0" stop-color="var(--gold-deep)"/>
        <stop offset="0.3" stop-color="var(--gold-mid)"/>
        <stop offset="0.5" stop-color="var(--gold-light)"/>
        <stop offset="0.7" stop-color="var(--gold-mid)"/>
        <stop offset="1" stop-color="var(--gold-deep)"/>
      </linearGradient>
      <linearGradient id="gold-text" x1="0" y1="0" x2="1" y2="1">
        <stop offset="0" stop-color="var(--gold-mid)"/>
        <stop offset="0.35" stop-color="var(--gold-deep)"/>
        <stop offset="0.55" stop-color="var(--gold-light)"/>
        <stop offset="0.8" stop-color="var(--gold-deep)"/>
        <stop offset="1" stop-color="var(--gold-mid)"/>
      </linearGradient>
      <radialGradient id="panel-fill" cx="0.5" cy="0.5" r="0.6">
        <stop offset="0" stop-color="var(--panel-glow)"/>
        <stop offset="1" stop-color="var(--panel-black)"/>
      </radialGradient>
      <path id="star" d="M0,-26 L6,-8 L25,-8 L10,4 L16,22 L0,11 L-16,22 L-10,4 L-25,-8 L-6,-8 Z"/>
    </defs>

    <!-- gold base -->
    <rect class="gold-base" x="0" y="0" width="944" height="1348" fill="url(#gold-band)"/>

    <!-- dark frame structure -->
    <g class="frame" fill="var(--frame-grey)">
      <rect x="24" y="238" width="896" height="872"/>
      <rect x="222" y="42" width="500" height="1264"/>
      <rect x="26" y="42" width="176" height="176"/>
      <rect x="742" y="42" width="176" height="176"/>
      <rect x="26" y="1130" width="176" height="176"/>
      <rect x="742" y="1130" width="176" height="176"/>
    </g>

    <!-- central black panel -->
    <g class="panel" fill="url(#panel-fill)">
      <rect x="58" y="256" width="828" height="836"/>
      <rect x="240" y="74" width="464" height="1200"/>
    </g>

    <!-- thin gold rules -->
    <g class="gold-rules" fill="var(--gold-mid)">
      <rect x="42" y="256" width="8" height="836"/>
      <rect x="894" y="256" width="8" height="836"/>
      <rect x="240" y="58" width="464" height="8"/>
      <rect x="240" y="1282" width="464" height="8"/>
    </g>

    <!-- corner ornament areas -->
    <g class="corner-ornaments">
      <rect x="44" y="60" width="140" height="140" fill="var(--gold-mid)"/>
      <rect x="52" y="68" width="124" height="124" fill="var(--ornament)" role="img" aria-label="Art deco rosette ornament"/>
      <rect x="760" y="60" width="140" height="140" fill="var(--gold-mid)"/>
      <rect x="768" y="68" width="124" height="124" fill="var(--ornament)" role="img" aria-label="Art deco rosette ornament"/>
      <rect x="44" y="1148" width="140" height="140" fill="var(--gold-mid)"/>
      <rect x="52" y="1156" width="124" height="124" fill="var(--ornament)" role="img" aria-label="Art deco rosette ornament"/>
      <rect x="760" y="1148" width="140" height="140" fill="var(--gold-mid)"/>
      <rect x="768" y="1156" width="124" height="124" fill="var(--ornament)" role="img" aria-label="Art deco rosette ornament"/>
    </g>

    <!-- stars -->
    <g class="stars" fill="url(#gold-text)">
      <use href="#star" x="383" y="172"/>
      <use href="#star" x="472" y="172"/>
      <use href="#star" x="560" y="172"/>
    </g>

    <!-- brand name -->
    <text class="brand-name" x="472" y="720" text-anchor="middle" fill="url(#gold-text)">Corvessa Cellars</text>

    <!-- volume -->
    <text class="volume-line" x="472" y="1126" text-anchor="middle" fill="url(#gold-text)">750 ml / ALC. 11% VOL</text>
  </svg>
</main>
</body>
</html>
```